Round Label Sticker 2.5-3 inch diameter

We need a design for a sticker to distribute for more brand recognition and product outreach.
My company The Bright Kettle Company Ltd. Specializes in working with people with diabetes. My products are made for diabetics because they have no added sugars, high in protein and fiber and each serving is lower than 5% daily value of carbohydrates.
I am a dietitian and my dad passed away from diabetes. I have created a growing food and beverage line that will give more joy into a diabetic's life while providing more food options that make them feel happy instead of guilty when they eat it.
I am teaching cooking classes to promote my products as well as doing exhibits and events. I want to give away a sticker to people that reads "I'm too sweet for sugar!" and somewhere on it would be my logo as well as my website info. www.brightkettle.example
The sticker should make people smile and warm as well as draw interest to my product line.
Target Market(s)
Diabetes and people who do not want added sugars in their food
Industry/Entity Type
Food Store
Requirements
Must have
- my logo and website

```html
<!DOCTYPE html>
<html lang="en">
<head>
<meta charset="utf-8">
<title>Bright Kettle – I'm too sweet for sugar sticker</title>
<link rel="stylesheet" href="https://fonts.googleapis.com/css2?family=Kaushan+Script&family=Open+Sans:wght@400;700&display=swap">
<style>
  :root {
    --paper: #ffffff;
    --plum: #3f006e;
    --plum-soft: #4e1584;
    --leaf: #7dc021;
    --cherry: #ff1a1a;
    --ink-shadow: #1a0030;
  }
  html, body {
    margin: 0;
    padding: 0;
    overflow: hidden;
    background: var(--paper);
  }
  .canvas {
    position: relative;
    width: 1200px;
    height: 1200px;
    overflow: hidden;
    background: var(--paper);
  }
  .sticker-shape {
    position: absolute;
    inset: 0;
  }
  .brand {
    position: absolute;
    left: 412px;
    top: 232px;
    width: 400px;
    display: flex;
    align-items: center;
    justify-content: center;
    gap: 12px;
  }
  .brand-dot {
    width: 18px;
    height: 18px;
    border-radius: 50%;
    background: var(--leaf);
  }
  .brand-name {
    font-family: "Open Sans", sans-serif;
    font-weight: 700;
    font-size: 40px;
    color: var(--plum);
    letter-spacing: 1px;
  }
  .slogan {
    position: absolute;
    left: 0;
    right: 0;
    margin: 0;
    text-align: center;
    font-family: "Kaushan Script", cursive;
    font-weight: 400;
    line-height: 1;
    text-shadow: 5px 4px 0 var(--ink-shadow);
  }
  .slogan-top {
    top: 395px;
    font-size: 118px;
    color: var(--leaf);
  }
  .slogan-accent {
    top: 545px;
    font-size: 138px;
    color: var(--cherry);
    letter-spacing: 2px;
  }
  .slogan-bottom {
    top: 690px;
    font-size: 118px;
    color: var(--leaf);
  }
  .website {
    position: absolute;
    left: 0;
    right: 0;
    top: 950px;
    margin: 0;
    text-align: center;
    font-family: "Open Sans", sans-serif;
    font-size: 28px;
    color: var(--paper);
  }
</style>
</head>
<body>
<main class="canvas">
  <svg class="sticker-shape" width="1200" height="1200" viewBox="0 0 1200 1200" aria-hidden="false">
    <defs>
      <clipPath id="sticker-edge">
        <circle cx="600" cy="600" r="450"/>
      </clipPath>
    </defs>
    <circle class="sticker-body" cx="600" cy="600" r="450" fill="var(--plum)"/>
    <g clip-path="url(#sticker-edge)">
      <circle class="logo-cap" cx="612" cy="140" r="196" fill="var(--paper)"/>
    </g>
    <circle class="sticker-rim" cx="600" cy="600" r="450" fill="none" stroke="var(--plum)" stroke-width="2"/>

    <g class="sweets-doodles" fill="var(--plum-soft)">
      <circle cx="345" cy="295" r="44" role="img" aria-label="Line drawing of a swirl lollipop"/>
      <circle cx="855" cy="318" r="44" role="img" aria-label="Line drawing of a cupcake"/>
      <circle cx="248" cy="455" r="46" role="img" aria-label="Line drawing of a muffin"/>
      <circle cx="905" cy="490" r="46" role="img" aria-label="Line drawing of cherries"/>
      <circle cx="258" cy="655" r="44" role="img" aria-label="Line drawing of a wrapped candy"/>
      <circle cx="980" cy="660" r="46" role="img" aria-label="Line drawing of a chocolate bar"/>
      <circle cx="355" cy="900" r="46" role="img" aria-label="Line drawing of a slice of cake"/>
      <circle cx="598" cy="882" r="46" role="img" aria-label="Line drawing of macarons"/>
      <circle cx="868" cy="870" r="46" role="img" aria-label="Line drawing of a round lollipop"/>
    </g>
  </svg>

  <div class="brand">
    <span class="brand-dot"></span>
    <span class="brand-name">Bright Kettle</span>
  </div>

  <h1 class="slogan slogan-top">I’m too</h1>
  <p class="slogan slogan-accent">SWEET</p>
  <p class="slogan slogan-bottom">for sugar!</p>

  <p class="website">www.brightkettle.example</p>
</main>
</body>
</html>
```